Wellpath Ledgers New Website

Please review the attached Design Brief with additional details. Thank you!

The goal is to create a website that effectively communicates the benefits of WellPath Ledgers to eye care professionals. The website should streamline the process of understanding and utilizing WellPath Ledgers' services, emphasizing improved patient outcomes, increased referrals, and enhanced patient engagement.

Target Market(s)

Eyecare Professionals

Number of Pages Required

4 page

```html
<!DOCTYPE html>
<html lang="en">
<head>
<meta charset="utf-8">
<title>Wellpath Ledgers</title>
<link href="https://fonts.googleapis.com/css2?family=Montserrat:wght@600;700;800&family=Poppins:wght@400;500;600&display=swap" rel="stylesheet">
<style>
:root{
  --blue:#0b6df6;
  --blue-deep:#0a3db5;
  --navy:#0d2a9e;
  --orange:#f8a532;
  --ink:#111318;
  --text:#3d4150;
  --cream:#fdf1e2;
  --white:#ffffff;
  --black:#000000;
}
*{margin:0;padding:0;box-sizing:border-box}
html,body{width:1200px;height:5079px;overflow:hidden}
body{position:relative;font-family:'Poppins',sans-serif;color:var(--text);background:var(--white)}
.abs{position:absolute}
h1,h2,h3,.heading{font-family:'Montserrat',sans-serif;font-weight:700;color:var(--ink)}
.accent{color:var(--orange)}
.btn{position:absolute;display:flex;align-items:center;justify-content:center;gap:8px;background:var(--orange);color:var(--white);font-family:'Montserrat',sans-serif;font-weight:700;font-size:11px;letter-spacing:.3px;border-left:4px solid var(--navy)}
.photo{position:absolute}
.check{display:flex;align-items:center;gap:14px;font-size:14px;color:var(--ink)}
.check svg{flex:none}

/* hero */
.hero{position:absolute;left:0;top:0;width:1200px;height:735px;background:linear-gradient(180deg,var(--blue) 0%,var(--blue-deep) 100%)}
.topbar{font-size:11px;color:var(--white);display:flex;align-items:center;gap:10px}
.nav a{position:absolute;top:72px;font-size:14px;color:var(--white);text-decoration:none}
.nav a.active{color:var(--orange)}
.logo-box{position:absolute;left:512px;top:0;width:180px;height:98px;background:var(--white);display:flex;align-items:center;justify-content:center;gap:8px}
.logo-box span{font-family:'Poppins',sans-serif;font-weight:600;font-size:18px;color:var(--blue-deep)}
.hero h1{position:absolute;left:124px;top:230px;font-size:46px;line-height:55px;color:var(--white)}
.hero p{position:absolute;left:122px;top:408px;width:300px;font-size:14px;line-height:22px;color:var(--white)}
.search{position:absolute;left:122px;top:512px;width:313px;height:44px;background:var(--white);border-radius:22px;font-size:11px;color:#777;padding-left:20px;display:flex;align-items:center}
.search i{position:absolute;right:0;top:0;width:44px;height:44px;border-radius:50%;background:var(--blue);display:flex;align-items:center;justify-content:center}
.badge{position:absolute;left:549px;top:339px;width:150px;height:150px;border-radius:50%;background:var(--navy);color:var(--white);text-align:center;padding-top:42px}
.badge b{font-family:'Montserrat',sans-serif;font-size:26px;display:block}
.badge span{font-size:13px;line-height:17px}

/* about */
.section-title{position:absolute;font-size:46px}
.about-copy{position:absolute;left:124px;top:920px;width:410px;font-size:14px;line-height:23px}

/* services */
.services{position:absolute;left:0;top:1393px;width:1200px;height:877px;background:linear-gradient(180deg,var(--blue) 0%,var(--blue-deep) 100%)}
.services .lead{position:absolute;left:130px;top:155px;width:400px;font-size:14px;line-height:23px;color:var(--white)}
.arrow-btn{position:absolute;width:44px;height:44px;border-radius:50%;display:flex;align-items:center;justify-content:center}
.svc{position:absolute;top:252px;width:302px;color:var(--white)}
.svc .num{text-align:right;font-family:'Montserrat',sans-serif;font-weight:700;font-size:26px;color:var(--orange);opacity:.7;height:24px}
.svc .num.on{opacity:1}
.svc .img{height:240px;margin-top:0}
.svc h3{color:var(--white);font-size:19px;margin-top:20px}
.svc p{font-size:13.5px;line-height:22px;margin-top:10px}
.svc a{display:flex;align-items:center;gap:8px;margin-top:22px;color:var(--orange);font-family:'Montserrat',sans-serif;font-weight:700;font-size:15px;text-decoration:none}

/* pricing */
.plan{position:absolute;top:2518px;width:302px;height:465px;background:var(--white);box-shadow:0 4px 18px rgba(0,0,0,.12)}
.plan .icon{width:84px;height:72px;background:var(--blue);display:flex;align-items:center;justify-content:center}
.plan h3{font-size:20px;margin:20px 0 0 20px}
.plan ul{list-style:none;margin:14px 0 0 22px}
.plan li{display:flex;align-items:center;gap:14px;font-size:12.5px;color:var(--ink);height:36px}
.price{margin:14px 0 0 26px;font-family:'Montserrat',sans-serif;font-weight:700;font-size:22px;color:var(--ink)}
.price sup{font-size:10px;color:var(--orange)}
.price small{display:block;font-family:'Poppins',sans-serif;font-weight:400;font-size:11px;color:#666;margin-top:-4px}

/* appointment */
.appt{position:absolute;left:124px;top:3083px;width:526px;height:701px;background:var(--cream);box-shadow:0 6px 20px rgba(0,0,0,.08)}
.field{position:absolute;left:43px;width:400px;height:40px;background:var(--white);border-radius:4px;font-size:11px;color:#555;padding:12px 16px}

/* testimonial */
.quote-box{position:absolute;left:479px;top:3966px;width:595px;height:293px;background:linear-gradient(180deg,var(--blue) 0%,var(--blue-deep) 100%);color:var(--white);padding:64px 100px 0 50px}

/* footer */
.footer{position:absolute;left:0;top:4442px;width:1200px;height:637px;background:var(--black);color:var(--white)}
.footer h3{color:var(--white);font-size:22px;position:absolute;top:218px}
.footer .links{position:absolute;left:563px;top:286px;font-size:12.5px;line-height:27.5px}
.contact-row{position:absolute;left:869px;display:flex;align-items:center;gap:16px;font-size:14px;line-height:22px}
.contact-row i{width:34px;height:34px;border-radius:50%;background:var(--white);display:flex;align-items:center;justify-content:center;flex:none}
.vline{position:absolute;top:248px;width:1px;height:222px;background:rgba(255,255,255,.6)}
.social{position:absolute;top:435px;width:24px;height:24px;border-radius:50%;background:var(--white)}
</style>
</head>
<body>

<!-- HERO -->
<header class="hero">
  <div class="topbar abs" style="left:124px;top:18px">
    <svg width="22" height="22" viewBox="0 0 22 22"><circle cx="11" cy="11" r="11" fill="#fff"/><path d="M11 5a4 4 0 0 0-4 4c0 3 4 8 4 8s4-5 4-8a4 4 0 0 0-4-4zm0 5.5a1.5 1.5 0 1 1 0-3 1.5 1.5 0 0 1 0 3z" fill="#0b6df6"/></svg>
    418 Marlow Bend Rd, Fairhaven, MS, 390112
  </div>
  <div class="topbar abs" style="left:820px;top:18px">
    <svg width="22" height="22" viewBox="0 0 22 22"><circle cx="11" cy="11" r="11" fill="#fff"/><circle cx="11" cy="11" r="6" fill="none" stroke="#0b6df6" stroke-width="2"/><path d="M11 8v3.5l2 1.5" stroke="#0b6df6" stroke-width="1.6" fill="none"/></svg>
    Opening Hours: Mon - Sat 8.00 - 18.00
  </div>
  <nav class="nav">
    <a class="active" style="left:124px">Home</a>
    <a style="left:206px">About Us</a>
    <a style="left:308px">Services</a>
    <a style="left:405px">Pricing</a>
    <a style="left:728px">Testimonials</a>
    <a style="left:851px">Blogs</a>
  </nav>
  <div class="logo-box"><svg width="12" height="12"><rect width="12" height="12" fill="#f8a532"/></svg><span>Wellpath Ledgers</span></div>
  <div class="btn" style="left:952px;top:60px;width:124px;height:40px">+ CONTACT US</div>

  <h1>The Best Eye<br><span class="accent">Doctors &amp;</span><br>Technology</h1>
  <p>Lorem Ipsum is simply dummy text of the printing and typesetting industry. Lorem Ipsum ha</p>
  <div class="search">Search Services<i><svg width="16" height="16" viewBox="0 0 16 16"><circle cx="7" cy="7" r="4.5" fill="none" stroke="#fff" stroke-width="1.5"/><path d="M10.5 10.5L14 14" stroke="#fff" stroke-width="1.5"/></svg></i></div>

  <div class="photo" role="img" aria-label="Patient looking into an eye examination instrument" style="left:626px;top:164px;width:448px;height:417px;background:linear-gradient(135deg,#e7ecef,#9fa8ae)"></div>
  <div class="photo" role="img" aria-label="Optometrist holding trial lens frame" style="left:528px;top:414px;width:215px;height:246px;background:linear-gradient(180deg,#d9d2cc,#b9b0aa)"></div>
  <div class="badge"><b>500+</b><span>Successfully<br>Eye Surgrey</span></div>
</header>

<!-- ABOUT -->
<section>
  <h2 class="section-title" style="left:126px;top:850px">About <span class="accent">Us</span></h2>
  <p class="about-copy">Lorem Ipsum is simply dummy text of the printing and typesetting industry. Lorem Ipsum has been the industry's standard dummy text ever since the 1500s, when an unknown printer took a galley of type and scrambled it to make a type specimen book. It has survive.</p>
  <div class="abs" style="left:124px;top:1080px;display:flex;flex-direction:column;gap:16px">
    <div class="check"><svg width="20" height="20"><circle cx="10" cy="10" r="10" fill="#eaf1fe"/><path d="M6 10l3 3 5-6" stroke="#0a3db5" stroke-width="2" fill="none"/></svg>V.EYE.P 360 EXAMS</div>
    <div class="check"><svg width="20" height="20"><circle cx="10" cy="10" r="10" fill="#eaf1fe"/><path d="M6 10l3 3 5-6" stroke="#0a3db5" stroke-width="2" fill="none"/></svg>EYE CARE AT EVERY AGE</div>
    <div class="check"><svg width="20" height="20"><circle cx="10" cy="10" r="10" fill="#eaf1fe"/><path d="M6 10l3 3 5-6" stroke="#0a3db5" stroke-width="2" fill="none"/></svg>EYEGLASSES AND CONTACT LENSES</div>
  </div>
  <div class="btn" style="left:126px;top:1219px;width:144px;height:40px">+ LEARN MORE</div>
  <div class="photo" role="img" aria-label="Doctor consulting a patient holding glasses" style="left:616px;top:833px;width:458px;height:458px;border-radius:50%;background:linear-gradient(135deg,#d8dde2,#8b939b)"></div>
  <svg class="abs" style="left:801px;top:1018px" width="88" height="88" viewBox="0 0 88 88"><circle cx="44" cy="44" r="44" fill="#0b6df6"/><path d="M36 30v28l22-14z" fill="#fff"/></svg>
</section>

<!-- SERVICES -->
<section class="services">
  <h2 class="section-title" style="left:126px;top:84px;color:#fff">What <span class="accent">We</span> DO</h2>
  <p class="lead">Lorem Ipsum is simply dummy text of the printing and typesetting industry. Lorem Ipsum ha</p>
  <div class="arrow-btn" style="left:951px;top:98px;border:1.5px solid #fff"><svg width="14" height="14"><path d="M9 2L4 7l5 5" stroke="#fff" stroke-width="1.6" fill="none"/></svg></div>
  <div class="arrow-btn" style="left:1016px;top:98px;background:var(--orange)"><svg width="14" height="14"><path d="M5 2l5 5-5 5" stroke="#fff" stroke-width="1.6" fill="none"/></svg></div>

  <div class="svc" style="left:124px">
    <div class="num">01</div>
    <div class="img" role="img" aria-label="Woman wearing trial frame during eye exam" style="background:linear-gradient(135deg,#eef0f1,#b8b2aa)"></div>
    <h3>Eye Exam</h3>
    <p>What is a Eye Exam? Neque gravida in fermentum et sollicitudin. Sit...</p>
    <a>Get Service <svg width="20" height="10"><path d="M0 5h17M13 1l4 4-4 4" stroke="#f8a532" stroke-width="1.6" fill="none"/></svg></a>
  </div>
  <div class="svc" style="left:449px">
    <div class="num on">02</div>
    <div class="img" role="img" aria-label="Surgeons performing laser eye surgery" style="background:linear-gradient(135deg,#dfe9ef,#7d96a8)"></div>
    <h3>Laser Eye Surgery</h3>
    <p>What is a Laser Eye Surgery? Laser eye surgery, or laser vision...</p>
    <a>Get Service <svg width="20" height="10"><path d="M0 5h17M13 1l4 4-4 4" stroke="#f8a532" stroke-width="1.6" fill="none"/></svg></a>
  </div>
  <div class="svc" style="left:772px">
    <div class="num">03</div>
    <div class="img" role="img" aria-label="Eye drops being applied for dry eye treatment" style="background:linear-gradient(135deg,#eef1f4,#d4b8a6)"></div>
    <h3>Dry Eye Surgery</h3>
    <p>What is a Dry Eye Surgery? Intense pulsed light therapy, or IPL...</p>
    <a>Get Service <svg width="20" height="10"><path d="M0 5h17M13 1l4 4-4 4" stroke="#f8a532" stroke-width="1.6" fill="none"/></svg></a>
  </div>
  <div class="btn" style="left:130px;top:711px;width:140px;height:40px;border-left:none">+ SEE ALL</div>
</section>

<!-- PRICING -->
<section>
  <h2 class="abs" style="left:0;top:2362px;width:1200px;text-align:center;font-size:44px">Pricing <span class="accent">&amp;</span> Plans</h2>
  <p class="abs" style="left:370px;top:2430px;width:460px;text-align:center;font-size:13.5px;line-height:22px;color:var(--ink)">Lorem Ipsum is simply dummy text of the printing and typesetting industry. Lorem Ipsum ha</p>

  <div class="plan" style="left:124px">
    <div class="icon"><svg width="30" height="30"><circle cx="15" cy="15" r="9" fill="none" stroke="#f8a532" stroke-width="3"/><circle cx="15" cy="15" r="3" fill="#f8a532"/></svg></div>
    <h3 style="margin-top:28px">Eye Treatment</h3>
    <ul>
      <li><svg width="18" height="18"><circle cx="9" cy="9" r="9" fill="#eaf1fe"/><path d="M5 9l3 3 5-6" stroke="#0a3db5" stroke-width="2" fill="none"/></svg>Regular Health Checkups</li>
      <li><svg width="18" height="18"><circle cx="9" cy="9" r="9" fill="#eaf1fe"/><path d="M5 9l3 3 5-6" stroke="#0a3db5" stroke-width="2" fill="none"/></svg>Free Equipment Use</li>
      <li><svg width="18" height="18"><circle cx="9" cy="9" r="9" fill="#eaf1fe"/><path d="M5 9l3 3 5-6" stroke="#0a3db5" stroke-width="2" fill="none"/></svg>Advance Options</li>
      <li><svg width="18" height="18"><circle cx="9" cy="9" r="9" fill="#eaf1fe"/><path d="M5 9l3 3 5-6" stroke="#0a3db5" stroke-width="2" fill="none"/></svg>GB Stage 16</li>
    </ul>
    <div class="price">59<sup>$</sup><small>Monthly</small></div>
    <div class="btn" style="left:20px;top:362px;width:144px;height:40px">+ CHOOSE PLAN</div>
  </div>

  <div class="plan" style="left:447px">
    <div class="icon"><svg width="30" height="30"><circle cx="12" cy="10" r="5" fill="#f8a532"/><path d="M3 27c0-7 4-11 9-11s9 4 9 11z" fill="#f8a532"/><circle cx="23" cy="8" r="4" fill="none" stroke="#f8a532" stroke-width="2"/></svg></div>
    <h3>Professional</h3>
    <ul>
      <li><svg width="18" height="18"><circle cx="9" cy="9" r="9" fill="#eaf1fe"/><path d="M5 9l3 3 5-6" stroke="#0a3db5" stroke-width="2" fill="none"/></svg>Regular Health Checkups</li>
      <li><svg width="18" height="18"><circle cx="9" cy="9" r="9" fill="#eaf1fe"/><path d="M5 9l3 3 5-6" stroke="#0a3db5" stroke-width="2" fill="none"/></svg>Free Equipment Use</li>
      <li><svg width="18" height="18"><circle cx="9" cy="9" r="9" fill="#eaf1fe"/><path d="M5 9l3 3 5-6" stroke="#0a3db5" stroke-width="2" fill="none"/></svg>Advance Options</li>
      <li><svg width="18" height="18"><circle cx="9" cy="9" r="9" fill="#eaf1fe"/><path d="M5 9l3 3 5-6" stroke="#0a3db5" stroke-width="2" fill="none"/></svg>GB Stage 16</li>
    </ul>
    <div class="price">69<sup>$</sup><small>Monthly</small></div>
    <div class="btn" style="left:20px;top:355px;width:144px;height:40px">+ CHOOSE PLAN</div>
  </div>

  <div class="plan" style="left:770px">
    <div class="icon"><svg width="30" height="30"><rect x="6" y="9" width="18" height="18" rx="2" fill="#f8a532"/><rect x="10" y="4" width="10" height="5" fill="#f8a532"/><path d="M15 13v10M10 18h10" stroke="#0b6df6" stroke-width="2.5"/></svg></div>
    <h3>Enterprice</h3>
    <ul>
      <li><svg width="18" height="18"><circle cx="9" cy="9" r="9" fill="#eaf1fe"/><path d="M5 9l3 3 5-6" stroke="#0a3db5" stroke-width="2" fill="none"/></svg>Regular Health Checkups</li>
      <li><svg width="18" height="18"><circle cx="9" cy="9" r="9" fill="#eaf1fe"/><path d="M5 9l3 3 5-6" stroke="#0a3db5" stroke-width="2" fill="none"/></svg>Free Equipment Use</li>
      <li><svg width="18" height="18"><circle cx="9" cy="9" r="9" fill="#eaf1fe"/><path d="M5 9l3 3 5-6" stroke="#0a3db5" stroke-width="2" fill="none"/></svg>Advance Options</li>
      <li><svg width="18" height="18"><circle cx="9" cy="9" r="9" fill="#eaf1fe"/><path d="M5 9l3 3 5-6" stroke="#0a3db5" stroke-width="2" fill="none"/></svg>GB Stage 16</li>
    </ul>
    <div class="price">79<sup>$</sup><small>Monthly</small></div>
    <div class="btn" style="left:20px;top:357px;width:144px;height:40px">+ CHOOSE PLAN</div>
  </div>
</section>

<!-- APPOINTMENT -->
<section>
  <div class="appt">
    <h2 class="abs" style="left:45px;top:60px;font-size:44px;line-height:55px">Make <span class="accent">An</span><br>Appointment</h2>
    <div class="field" style="top:199px">Your Name</div>
    <div class="field" style="top:253px">Enter Email</div>
    <div class="field" style="top:307px">Subject</div>
    <div class="field" style="top:361px">Phone</div>
    <div class="field" style="top:416px;height:148px">Message</div>
    <div class="btn" style="left:49px;top:595px;width:140px;height:41px;background:var(--navy);border-left-color:var(--orange)">+ SUBMIT</div>
  </div>
  <div class="photo" role="img" aria-label="Smiling doctor in scrubs with stethoscope" style="left:611px;top:3148px;width:461px;height:572px;background:linear-gradient(180deg,#2d2a2a,#6a7b8e)"></div>
</section>

<!-- TESTIMONIALS -->
<section>
  <h2 class="abs" style="left:0;top:3872px;width:1200px;text-align:center;font-size:44px"><span class="accent" style="font-weight:600">Our</span> Testimonials</h2>
  <div class="photo" role="img" aria-label="Portrait of a smiling patient" style="left:124px;top:3966px;width:302px;height:293px;background:linear-gradient(180deg,#4e4a48,#c77a72)"></div>
  <div class="quote-box">
    <p style="font-size:13.5px;line-height:22px">Lorem Ipsum is simply dummy text of the printing and typesetting industry. Lorem Ipsum has been the industry's standard dummy text ever since the 1500s,</p>
    <div style="color:var(--orange);font-size:18px;letter-spacing:5px;margin-top:24px">★★★★★</div>
    <div style="font-family:'Montserrat',sans-serif;font-weight:600;font-size:19px;margin-top:10px">Mara Linden</div>
    <div style="font-size:10px;color:var(--orange)">OUR PATIENT</div>
  </div>
  <svg class="abs" style="left:437px;top:4060px" width="84" height="84" viewBox="0 0 84 84"><circle cx="42" cy="42" r="42" fill="#f8a532"/><path d="M28 32h11v11l-5 10h-6l4-10h-4zM45 32h11v11l-5 10h-6l4-10h-4z" fill="#0d2a9e"/></svg>
  <div class="arrow-btn" style="left:965px;top:4298px;border:1.5px solid #333"><svg width="14" height="14"><path d="M9 2L4 7l5 5" stroke="#333" stroke-width="1.6" fill="none"/></svg></div>
  <div class="arrow-btn" style="left:1032px;top:4298px;background:var(--orange)"><svg width="14" height="14"><path d="M5 2l5 5-5 5" stroke="#fff" stroke-width="1.6" fill="none"/></svg></div>
</section>

<!-- FOOTER -->
<footer class="footer">
  <div class="abs" style="left:128px;top:112px;display:flex;align-items:center;gap:10px"><svg width="14" height="14"><rect width="14" height="14" fill="#fff"/></svg><span style="font-weight:600;font-size:26px">Wellpath Ledgers</span></div>
  <h3 style="left:132px">About Us</h3>
  <p class="abs" style="left:132px;top:264px;width:270px;font-size:13.5px;line-height:22px">Lorem Ipsum is simply dummy text of the printing and typesetting industry. Lorem Ipsum has been the industry's</p>
  <span class="social" style="left:125px"></span>
  <span class="social" style="left:167px"></span>
  <span class="social" style="left:209px"></span>
  <div class="vline" style="left:479px"></div>
  <h3 style="left:563px">Quick Links</h3>
  <div class="links">Home<br>About Us<br>Services<br>Pricing<br>Testimonials<br>Blogs<br>FAQs<br>Contact Us</div>
  <div class="vline" style="left:782px"></div>
  <h3 style="left:869px">Contact Us</h3>
  <div class="contact-row" style="top:269px"><i><svg width="14" height="14" viewBox="0 0 14 14"><path d="M3 1l2 3-1.5 1.5a8 8 0 0 0 5 5L10 9l3 2-1 2c-6 0-11-5-11-11z" fill="#000"/></svg></i>555-210-4471</div>
  <div class="contact-row" style="top:334px"><i><svg width="14" height="14"><rect x="1" y="3" width="12" height="8" fill="#000"/><path d="M1 3l6 5 6-5" stroke="#fff" fill="none"/></svg></i>Info@WellPathLedgers.com</div>
  <div class="contact-row" style="top:399px"><i><svg width="14" height="14" viewBox="0 0 14 14"><path d="M7 1a4 4 0 0 0-4 4c0 3 4 8 4 8s4-5 4-8a4 4 0 0 0-4-4zm0 5.5a1.5 1.5 0 1 1 0-3 1.5 1.5 0 0 1 0 3z" fill="#000"/></svg></i>12B Thornfield Street,<br>Ashvale 4021</div>
  <div class="abs" style="left:124px;top:564px;width:1034px;height:1px;background:rgba(255,255,255,.5)"></div>
  <p class="abs" style="left:0;top:590px;width:1200px;text-align:center;font-size:13px">© Copyright 2023 <b>Wellpath Ledgers</b> . All Rights Reserved</p>
</footer>

</body>
</html>
```